Etiketten-Design für Wein
Zielgruppe
Wir produzieren Wein und sind auf der Suche nach einer innovativen Weinetikette, welche sich durch unsere Weinvariationen durchziehen lässt.
Für das stehen wir ein: Nachhaltigkeit, moderne Landwirtschaft, Familienbetrieb, zukunftsorientiert, im Einklang mi der Natur, Freude an Pflanzen und Tieren.
Was uns gefällt: Relief / Prägung, eher schlichte, moderne und edle Etiketten, allenfalls Elemente aus der Natur, die auf Nachhaltigkeit hinweisen
Das möchten wir nicht auf der Etikette: zu knallige Farben, Comicfiguren oder ähnliches.
Unsere Weine werden direkt vermarktet und sollen aufgrund ihrer Etikette aus dem Weinregal herausstechen und ein Eyecatcher für die Kund:innen sein. Auch in einem Restaurant sollen sie als edlen Wein präsentiert werden können. Wir möchten, dass die Weinetiketten ein Storytelling mit sich bringen in Bezug auf die obenstehenden Punkte, für die wir einstehen.
Unsere Zielgruppe: Qualitätsbewusste Weingeniesser, mittleren und jüngeren Alters
Aufgabenstellung
Folgende Angaben sind auf der Etikette erforderlich:
- Weinsorte: Reserva / Riesling / Blauburgunder / Federweisser
- Name: Sennbachgut (kann klein und schlicht, unauffällig sein)
Unser Logo kann in Etikette aufgegriffen werden (auch in angepasster Form), ist aber nicht zwingend nötig. Das Logo ist auch eher revisionsbedürftig. ????
Folgende Masse sollte die Etikette ca. haben:
- Breite 95 mm
- Höhe 80 mm

```html
<!DOCTYPE html>
<html lang="de">
<head>
<meta charset="utf-8">
<title>Sennbachgut – Etiketten</title>
<link rel="stylesheet" href="https://fonts.googleapis.com/css2?family=Playfair+Display:wght@800&family=Montserrat:wght@400&display=swap">
<style>
  :root {
    --backdrop: #2b2628;
    --paper: #f4f1f1;
    --paper-shade: #e9e4e5;
    --ink: #1f1b1c;
    --leaf-rose: rgba(176, 92, 98, 0.22);
    --leaf-copper: rgba(196, 118, 96, 0.22);
  }
  * { margin: 0; padding: 0; box-sizing: border-box; }
  html, body {
    width: 1200px;
    height: 900px;
    overflow: hidden;
  }
  body {
    background: var(--backdrop);
    display: flex;
    align-items: center;
    justify-content: center;
    gap: 40px;
  }
  .label {
    position: relative;
    width: 330px;
    height: 278px;
    background: linear-gradient(160deg, var(--paper) 0%, var(--paper-shade) 100%);
    overflow: hidden;
  }
  .leaf {
    position: absolute;
    width: 120px;
    height: 110px;
    border-radius: 50%;
  }
  .leaf--rose { background: radial-gradient(circle, var(--leaf-rose) 0%, rgba(176, 92, 98, 0) 70%); }
  .leaf--copper { background: radial-gradient(circle, var(--leaf-copper) 0%, rgba(196, 118, 96, 0) 70%); }
  .leaf--top-left { top: 4px; left: 8px; }
  .leaf--top-right { top: -6px; right: -18px; }
  .leaf--bottom-right { bottom: -12px; right: 14px; width: 150px; }
  .leaf--bottom-left { bottom: -10px; left: 0; }

  .wordmark {
    position: absolute;
    text-align: center;
    color: var(--ink);
  }
  .wordmark__estate {
    font-family: "Montserrat", sans-serif;
    font-weight: 400;
    font-size: 8px;
    letter-spacing: 0.28em;
    text-transform: uppercase;
    display: block;
    margin-bottom: 3px;
  }
  .wordmark__variety {
    font-family: "Playfair Display", serif;
    font-weight: 800;
    font-size: 26px;
    line-height: 1.05;
    display: block;
  }
  .label--reserva .wordmark { top: 136px; left: 96px; width: 170px; }
  .label--riesling .wordmark { top: 102px; left: 0; width: 100%; }
</style>
</head>
<body>
  <div class="label label--reserva">
    <div class="leaf leaf--rose leaf--top-left" role="img" aria-label="Feine Strichzeichnung eines Weinblatts"></div>
    <div class="wordmark">
      <span class="wordmark__estate">Sennbachgut</span>
      <span class="wordmark__variety">Reserva.</span>
    </div>
    <div class="leaf leaf--rose leaf--bottom-right" role="img" aria-label="Feine Strichzeichnung von Weinblättern"></div>
  </div>

  <div class="label label--riesling">
    <div class="leaf leaf--copper leaf--top-right" role="img" aria-label="Feine Strichzeichnung eines Weinblatts in Kupfer"></div>
    <div class="wordmark">
      <span class="wordmark__estate">Sennbachgut</span>
      <span class="wordmark__variety">Riesling<br>Silvaner.</span>
    </div>
    <div class="leaf leaf--copper leaf--bottom-left" role="img" aria-label="Feine Strichzeichnung eines Weinblatts in Kupfer"></div>
  </div>

  <div class="label label--reserva">
    <div class="leaf leaf--rose leaf--top-left" role="img" aria-label="Feine Strichzeichnung eines Weinblatts"></div>
    <div class="wordmark">
      <span class="wordmark__estate">Sennbachgut</span>
      <span class="wordmark__variety">Reserva.</span>
    </div>
    <div class="leaf leaf--rose leaf--bottom-right" role="img" aria-label="Feine Strichzeichnung von Weinblättern"></div>
  </div>
</body>
</html>
```